PlumVerse Business Cards

I need a business card designed for PlumVerse. To get an idea of what we do please visit https://brisklayout.example/para-artistas-7

```html
<!DOCTYPE html>
<html lang="en">
<head>
<meta charset="utf-8">
<title>PlumVerse Business Card</title>
<link href="https://fonts.googleapis.com/css2?family=Montserrat:wght@300;400;500;600;700&display=swap" rel="stylesheet">
<style>
  :root {
    --backdrop: #3b3b3b;
    --card: #161616;
    --accent: #f0a020;
    --text-light: #e8e8e8;
    --text-muted: #bdbdbd;
    --pattern-dark: #1c1c1c;
    --pattern-mid: #2a2a2a;
  }
  * { margin: 0; padding: 0; box-sizing: border-box; }
  html, body {
    width: 1200px; height: 801px; overflow: hidden;
    background: var(--backdrop);
    font-family: "Montserrat", sans-serif;
  }
  .sheet {
    width: 1200px; height: 801px;
    display: flex; align-items: center; justify-content: center; gap: 40px;
  }
  .card {
    position: relative;
    width: 520px; height: 297px;
    background: var(--card);
    border: 2px solid var(--accent);
    overflow: hidden;
  }
  /* Front */
  .brand {
    position: absolute; left: 60px; top: 70px;
    display: flex; align-items: center; gap: 22px;
  }
  .brand-square {
    width: 52px; height: 52px;
    border: 2px solid var(--accent);
  }
  .brand-name {
    font-weight: 400; font-size: 30px; letter-spacing: 9px;
    color: var(--text-light); text-transform: uppercase;
  }
  .tagline {
    position: absolute; left: 135px; top: 118px;
    font-size: 8px; letter-spacing: 5px; font-weight: 500;
    color: var(--accent); text-transform: uppercase;
  }
  .tagline-rule {
    position: absolute; left: 272px; top: 122px;
    width: 200px; height: 1px; background: var(--text-muted);
  }
  .person {
    position: absolute; right: 236px; top: 205px; text-align: right;
  }
  .person-name {
    font-weight: 700; font-size: 20px; color: var(--accent);
    text-transform: uppercase; letter-spacing: 0.3px;
  }
  .person-role {
    font-size: 13px; color: var(--text-light); margin-top: 2px;
  }
  .divider {
    position: absolute; left: 300px; top: 196px;
    width: 2px; height: 64px; background: var(--accent);
  }
  .contacts {
    position: absolute; left: 318px; top: 196px;
    list-style: none;
  }
  .contacts li {
    display: flex; align-items: center; gap: 8px;
    font-size: 12.5px; color: var(--text-light); line-height: 21px;
  }
  .contacts svg { width: 11px; height: 11px; fill: var(--accent); flex: none; }
  /* Back */
  .pattern-field {
    position: absolute; inset: 0;
    background: linear-gradient(120deg, var(--pattern-dark) 0%, var(--pattern-mid) 55%, var(--pattern-dark) 100%);
  }
  .back-brand {
    position: absolute; right: 44px; top: 120px;
    font-size: 18px; font-weight: 400; letter-spacing: 4px;
    color: var(--accent); text-transform: uppercase;
  }
</style>
</head>
<body>
<main class="sheet">
  <section class="card card-front" aria-label="Card front">
    <div class="brand">
      <div class="brand-square"></div>
      <div class="brand-name">PlumVerse</div>
    </div>
    <div class="tagline">Digital Notary</div>
    <div class="tagline-rule"></div>

    <div class="person">
      <div class="person-name">Nora Castellan</div>
      <div class="person-role">President</div>
    </div>
    <div class="divider"></div>
    <ul class="contacts">
      <li>
        <svg viewBox="0 0 24 24" aria-hidden="true"><path d="M6.6 10.8a15.1 15.1 0 0 0 6.6 6.6l2.2-2.2c.3-.3.7-.4 1-.2 1.1.4 2.3.6 3.6.6.6 0 1 .4 1 1V20c0 .6-.4 1-1 1A17 17 0 0 1 3 4c0-.6.4-1 1-1h3.5c.6 0 1 .4 1 1 0 1.3.2 2.5.6 3.6.1.3 0 .7-.2 1z"/></svg>
        555-014-2270
      </li>
      <li>
        <svg viewBox="0 0 24 24" aria-hidden="true"><path d="M2 5h20v14H2z M2 5l10 8 10-8" fill="var(--accent)"/><path d="M3 6l9 7 9-7" fill="none" stroke="#161616" stroke-width="2"/></svg>
        nora@plumverse.example
      </li>
      <li>
        <svg viewBox="0 0 24 24" aria-hidden="true"><circle cx="12" cy="12" r="10"/><path d="M2 12h20M12 2c3 3 3 17 0 20M12 2c-3 3-3 17 0 20" fill="none" stroke="#161616" stroke-width="1.6"/></svg>
        www.plumverse.example
      </li>
    </ul>
  </section>

  <section class="card card-back" aria-label="Card back">
    <div class="pattern-field" role="img" aria-label="Tone-on-tone repeating geometric pattern in dark grey"></div>
    <div class="back-brand">PlumVerse</div>
  </section>
</main>
</body>
</html>
```